Corporate Capability Statement

We have developed a capability statement - it is consistent with our corporate branding (refer www.brelvixo.com.au) but it could do with some professional formatting.

We need a print ready Word and PDF document that we can send to printers to arrange for large volume print.

Our profile is professional + high quality with a hint of creative!

```html
<!DOCTYPE html>
<html lang="en">
<head>
<meta charset="utf-8">
<title>Brelvixo Case Studies: M&amp;A</title>
<link href="https://fonts.googleapis.com/css2?family=Montserrat:wght@600;700&family=Questrial&family=Arimo:wght@400;700&display=swap" rel="stylesheet">
<style>
:root{
  --navy:#1b3651;
  --navy-dark:#14304b;
  --cell:#5b9bd5;
  --panel:#dde3ee;
  --ink:#1a1a1a;
  --line:#5a5a5a;
  --white:#ffffff;
}
*{box-sizing:border-box;margin:0;padding:0}
html,body{width:884px;height:1200px;overflow:hidden;background:var(--white)}
body{position:relative;font-family:"Questrial",sans-serif;color:var(--ink)}
.page-header{position:absolute;left:24px;top:0;width:837px;height:105px;background:var(--navy);color:var(--white)}
.page-title{position:absolute;left:10px;top:17px;font-family:"Montserrat",sans-serif;font-weight:600;font-size:20.5px;line-height:27px}
.page-number{position:absolute;right:30px;top:34px;font-family:"Montserrat",sans-serif;font-weight:700;font-size:20px}
.case-studies{position:absolute;left:33px;top:117px;font-size:15.5px;line-height:19.5px}
.case-studies h2{font-family:"Montserrat",sans-serif;font-weight:600;font-size:15px}
.case-studies ol{padding-left:56px}
.case-studies li{padding-left:6px}
.profile{position:absolute;left:24px;top:210px;width:837px;height:470px;border:1px solid var(--line)}
.profile-heading{position:absolute;left:16px;top:4px;font-family:"Montserrat",sans-serif;font-weight:600;font-size:18px;color:var(--navy)}
.member-name{position:absolute;left:16px;top:64px;font-family:"Montserrat",sans-serif;font-weight:700;font-size:13.5px}
.member-office{position:absolute;left:16px;top:90px;font-size:14px}
.member-photo{position:absolute;left:238px;top:54px;width:161px;height:136px;background:linear-gradient(#e9e9e9,#c9c9c9);border:4px solid var(--navy)}
.member-quals{position:absolute;left:435px;top:64px;width:185px;font-size:14px;line-height:17.5px}
.member-exp{position:absolute;left:635px;top:64px;width:160px;font-size:14px;line-height:17.5px}
.member-bio{position:absolute;left:16px;top:198px;width:803px;font-size:13.6px;line-height:17.4px;text-align:justify}
.member-bio p{margin-bottom:9px}
.methodology{position:absolute;left:24px;top:699px;width:837px;height:468px;background:var(--panel);border:1px solid var(--line)}
.methodology-heading{position:absolute;left:8px;top:3px;font-family:"Montserrat",sans-serif;font-weight:700;font-size:14.5px}
.flow{position:absolute;left:10px;top:20px;width:788px;height:225px;background:var(--white)}
.flow text{font-family:"Questrial",sans-serif;font-size:14px;fill:var(--white);text-anchor:middle}
.phase-table{position:absolute;left:20px;top:258px;width:798px;border-collapse:separate;border-spacing:1px;background:var(--white);font-family:"Arimo",sans-serif;font-size:11px;line-height:13.7px;color:var(--white)}
.phase-table th{background:var(--navy-dark);text-align:left;vertical-align:top;font-weight:700;padding:5px 8px;height:48px}
.phase-table td{background:var(--cell);vertical-align:top;padding:5px 8px;height:134px}
.phase-table td.row-label{background:var(--navy-dark);font-weight:700}
.figure-caption{position:absolute;left:8px;top:448px;font-family:"Montserrat",sans-serif;font-weight:700;font-size:13px}
</style>
</head>
<body>
<header class="page-header">
  <h1 class="page-title">Brelvixo Case Studies: M&amp;A<br>(Divestments, Mergers and Acquisitions)</h1>
  <div class="page-number">4</div>
</header>

<section class="case-studies">
  <h2>Case Studies:</h2>
  <ol>
    <li>Acquisition of assets by an International trade buyer</li>
    <li>Acquisition by a private equity roll-up</li>
    <li>Staged merger and acquisition</li>
  </ol>
</section>

<section class="profile">
  <h2 class="profile-heading">Brelvixo Team Member Profile</h2>
  <div class="member-name">Alan Brennick</div>
  <div class="member-office">Brelvixo Victoria</div>
  <div class="member-photo" role="img" aria-label="Portrait photograph of team member"></div>
  <div class="member-quals">BBus, CPA, FACA, MAICD, AFAIM</div>
  <div class="member-exp">35 years M&amp;A and corporate finance experience</div>
  <div class="member-bio">
    <p>Alan started his professional career in 1972 as an auditor with a precedent firm of Harwell &amp; Co's. Moving into industry in 1975 he worked as a financial accountant then as the surety underwriter for Orbis Insurance Victoria. In 1978 Alan joined Meridia Bank and became Regional Head of Credit for WA, SA &amp; NT. From 1982 to 1989 he was involved in a number of businesses with partners in the financial broking, wealth management, superannuation administration, property, business broking and corporate finance areas, culminating with the NXE listing of the business, Lantern Hill Limited where Alan held the position of Managing Director/CEO.</p>
    <p>After the takeover of Lantern Hill, Alan joined Calder Partners where he became a Partner in their Corporate Finance division then National Head of Mergers &amp; Acquisitions and established offices in each state. In 2002 Alan established the Private Equity Division becoming Head of Private Equity (Corporate Finance) and held this role until his retirement in 2012. During his time at Calder Partners Alan was lead advisor on over 150 transactions across 30+ industries with a combined value of over $5bn.</p>
    <p>Alan is an experienced executive director, CEO and chair with over 25 years board level experience. He has sat on the board or committees of over 15 separate organisations spanning: listed; private; not for profit; and government (State &amp; Federal) sectors. He has managed listed and private companies and divisions.</p>
  </div>
</section>

<section class="methodology">
  <h2 class="methodology-heading">Brelvixo's Acquisition Methodology:</h2>
  <svg class="flow" viewBox="0 0 788 225" width="788" height="225">
    <g fill="#1b3651">
      <polygon points="7,28 144,28 169,60 144,92 7,92 32,60"/>
      <polygon points="152,28 289,28 314,60 289,92 152,92 177,60"/>
      <polygon points="298,28 435,28 460,60 435,92 298,92 323,60"/>
      <polygon points="442,28 579,28 604,60 579,92 442,92 467,60"/>
      <polygon points="588,28 725,28 750,60 725,92 588,92 613,60"/>
      <polygon points="588,179 613,147 750,147 725,179 750,211 613,211"/>
      <polygon points="443,179 468,147 605,147 580,179 605,211 468,211"/>
    </g>
    <g fill="none" stroke="#1b3651" stroke-width="2.2">
      <polyline points="455,32 455,12 505,12 505,22"/>
      <polyline points="509,96 509,112 459,112 459,102"/>
      <polyline points="752,60 764,60 764,179 754,179"/>
    </g>
    <g fill="#1b3651">
      <polygon points="500,21 510,21 505,27"/>
      <polygon points="454,103 464,103 459,97"/>
      <polygon points="756,174 756,184 750,179"/>
    </g>
    <text x="100" y="57">Acquistion</text><text x="100" y="74">Strategy</text>
    <text x="243" y="58">Candidate</text><text x="243" y="75">Targeting</text>
    <text x="388" y="57">Candidate</text><text x="388" y="74">Sourcing</text>
    <text x="532" y="56">Candidate</text><text x="532" y="73">Qualification</text>
    <text x="672" y="44">Offer,</text><text x="672" y="58">Negotiation</text><text x="672" y="72">and</text><text x="672" y="86">Diligence</text>
    <text x="530" y="184">Transact</text>
    <text x="674" y="163">Post</text><text x="674" y="180">Acquisition</text><text x="674" y="197">Integration</text>
  </svg>

  <table class="phase-table">
    <tr>
      <th style="width:86px">Phase</th>
      <th>Acquisition Strategy</th>
      <th>Candidate Targeting</th>
      <th>Candidate Sourcing</th>
      <th>Candidate Qualification</th>
      <th>Offer, Negotiation and Diligence</th>
      <th>Transact</th>
      <th>Post Acquisition Integration</th>
    </tr>
    <tr>
      <td class="row-label">Example Actions</td>
      <td>✓Objectives<br>✓Targets<br>✓Financial Structure<br>✓Integration Strategy</td>
      <td>✓Scope<br>✓Size<br>✓Geography<br>✓Financial<br>✓Key criteria (“5 Pillars”)</td>
      <td>✓Source candidates (Brelvixo network, direct, indirect etc)<br>✓EOI</td>
      <td>✓Specific client criteria<br>✓“5 Pillars”<br>✓DRA<br>✓Specific industry criteria</td>
      <td>✓Establish common deal parameters<br>✓Negotiate<br>✓LOI<br>✓Due Diligence</td>
      <td>✓Contract<br>✓Project manage accounting and legal processes<br>✓Completion conditions<br>✓Complete</td>
      <td>✓PMI Plan<br>✓Bed-down<br>✓Performance reporting<br>✓Harvest synergies<br>✓Look-back</td>
    </tr>
  </table>
  <div class="figure-caption">Figure: Brelvixo's Acquisition Methodology</div>
</section>
</body>
</html>
```